Business Card Design

Hello!
We would like you to design some business cards for us. We will send you a sample of what we have. We want to take out the Tidewell Harbor Logo and add the RZD logo. This is the company that we own and it manages 7 to 8 franchised child care locations called Pebble Grove. So you can make the Pebble Grove a little logo smaller than what it currently is. Currently the back of the card lists the locations but we don't need that as we are adding new locations every few months. We can also add the website address for RZD below the logo if needed. We don't like the current design so please change it up as you like. Please let us know if you have any questions.

Industry/Entity Type

Business

Contact Information for Business Card

See above

Font styles to use
Serif
Sans Serif

Colors

Designer to choose colors to be used in the design.

Requirements
Must have
• Clean crisp look

```html
<!DOCTYPE html>
<html lang="en">
<head>
<meta charset="utf-8">
<title>Pebble Grove – Business Cards</title>
<link rel="stylesheet" href="https://fonts.googleapis.com/css2?family=Montserrat:wght@500;700&display=swap">
<style>
  :root{
    --stage:#3b3140;
    --card:#ffffff;
    --red:#c8102e;
    --ink:#1b1b1b;
  }
  *{margin:0;padding:0;box-sizing:border-box}
  html,body{width:1200px;height:800px;overflow:hidden}
  body{background:var(--stage);font-family:"Montserrat",sans-serif;position:relative}
  .card{position:absolute;top:250px;width:525px;height:300px;background:var(--card);
        box-shadow:0 6px 18px rgba(0,0,0,.35);overflow:hidden}
  .card--front{left:45px}
  .card--back{left:630px}

  .brand{position:absolute;display:flex;align-items:center;gap:12px}
  .brand__mark{flex:none;background:var(--red);border-radius:50%}
  .brand__name{font-weight:700;color:var(--red);line-height:1;white-space:nowrap}

  .card--front .brand{left:34px;top:34px}
  .card--front .brand__mark{width:22px;height:22px}
  .card--front .brand__name{font-size:34px}

  .mgmt{position:absolute;display:flex;align-items:center;gap:8px}
  .mgmt__mark{flex:none;width:14px;height:14px;background:var(--red)}
  .mgmt__name{font-weight:700;color:var(--red);text-transform:uppercase;line-height:1.2}
  .card--front .mgmt{left:34px;top:140px}
  .card--front .mgmt__name{font-size:13px}

  .contact{position:absolute;left:270px;top:104px;color:var(--ink)}
  .contact__name{font-weight:700;color:var(--red);font-size:22px;line-height:1}
  .contact__title{font-weight:500;font-size:12px;margin-top:4px;margin-bottom:10px}
  .contact__row{display:flex;align-items:flex-start;gap:10px;font-size:11px;font-weight:500;margin-bottom:7px;line-height:1.35}
  .contact__row span{padding-top:3px}
  .contact__icon{flex:none;width:22px;height:22px}

  .card--back .brand{left:0;right:0;top:96px;justify-content:center}
  .card--back .brand__mark{width:28px;height:28px}
  .card--back .brand__name{font-size:48px}
  .card--back .mgmt{left:0;right:0;top:186px;justify-content:center}
  .card--back .mgmt__mark{width:18px;height:18px}
  .card--back .mgmt__name{font-size:16px}
</style>
</head>
<body>
  <section class="card card--front">
    <div class="brand">
      <span class="brand__mark"></span>
      <span class="brand__name">Pebble Grove</span>
    </div>

    <div class="mgmt">
      <span class="mgmt__mark"></span>
      <span class="mgmt__name">Rowan Zephyr<br>Management</span>
    </div>

    <div class="contact">
      <div class="contact__name">Dara Kellen</div>
      <div class="contact__title">Academy Owner</div>
      <div class="contact__row">
        <svg class="contact__icon" viewBox="0 0 22 22"><circle cx="11" cy="11" r="11" fill="var(--red)"/><path d="M8 6.5c.6-.4 1.2-.2 1.5.4l.8 1.6c.2.5 0 1-.4 1.3l-.5.4c.5 1.2 1.4 2.1 2.6 2.6l.4-.5c.3-.4.8-.6 1.3-.4l1.6.8c.6.3.8.9.4 1.5-.6 1-1.7 1.4-2.8 1-2.6-.9-4.6-2.9-5.5-5.5-.4-1.1 0-2.2.6-3.2z" fill="#fff"/></svg>
        <span>555-014-2270</span>
      </div>
      <div class="contact__row">
        <svg class="contact__icon" viewBox="0 0 22 22"><circle cx="11" cy="11" r="11" fill="var(--red)"/><rect x="5.5" y="7" width="11" height="8" fill="none" stroke="#fff" stroke-width="1.4"/><path d="M5.5 7l5.5 4.5L16.5 7" fill="none" stroke="#fff" stroke-width="1.4"/></svg>
        <span>dara.kellen@pebblegrove.example</span>
      </div>
      <div class="contact__row">
        <svg class="contact__icon" viewBox="0 0 22 22"><circle cx="11" cy="11" r="11" fill="var(--red)"/><path d="M5.5 11.5L11 6.5l5.5 5h-1.8V16h-2.6v-3h-2.2v3H7.3v-4.5z" fill="#fff"/></svg>
        <span>Management Offices<br>418 Larkspur Avenue, Suite G<br>Maple Ridge, IL 60000</span>
      </div>
    </div>
  </section>

  <section class="card card--back">
    <div class="brand">
      <span class="brand__mark"></span>
      <span class="brand__name">Pebble Grove</span>
    </div>
    <div class="mgmt">
      <span class="mgmt__mark"></span>
      <span class="mgmt__name">Rowan Zephyr<br>Management</span>
    </div>
  </section>
</body>
</html>
```